Cafe menu design

Hi there,

We need a editable menu layout and design to match our new cafe call: " Harlow Bean Roasters", we love the ideas of A4 clip board and self print out menu in black and white. ( Example as attached)

We would like the menu can be break down into category easy for customer to flip around and read. ( example as attached)

Category including the following:

- All day breakfast and Sandwich and Toast
- Main (Lunch&Dinner) and Pizza
- Dessert snacks and nibbles
- Hot and Cold Drinks
- Catering menu

Please find our logo and our current menu as attached for your information and convenience.
Updates

Dear Designers, Thank you for your time and submission, Please find our drink menu and logo as attached. Kind Regards,

Target Market(s)

Young family, young Couple, office and corporate staff

Industry/Entity Type

Cafe

Font styles to use
Serif
Sans Serif

```html
<!DOCTYPE html>
<html lang="en">
<head>
<meta charset="utf-8">
<title>Harlow Bean Roasters — All day breakfast and Sandwich and Toast</title>
<link rel="stylesheet" href="https://fonts.googleapis.com/css2?family=Arimo:wght@400;700&family=Tinos&display=swap">
<style>
  :root {
    --ink: #1a1a1a;
    --black: #141414;
    --paper: #ffffff;
    --price-band: #d2d2d2;
    --rule: #e0e0e0;
    --muted: #7a7a7a;
    --edge: #9a9a9a;
  }
  * { box-sizing: border-box; margin: 0; padding: 0; }
  html, body { width: 873px; height: 1200px; overflow: hidden; background: var(--paper); }
  body { position: relative; font-family: "Arimo", Arial, sans-serif; color: var(--ink); }

  .sidebar { position: absolute; left: 0; top: 0; width: 174px; height: 1113px; border-right: 1px solid var(--edge); }
  .brand { position: absolute; left: 0; top: 22px; width: 174px; text-align: center; }
  .brand-dot { display: block; width: 58px; height: 58px; border-radius: 50%; background: var(--black); margin: 0 auto 12px; }
  .brand-name { font-weight: 700; font-size: 17px; line-height: 21px; color: var(--black); text-transform: uppercase; letter-spacing: 1px; }
  .order-note { position: absolute; left: 0; top: 206px; width: 190px; text-align: center; font-family: "Tinos", "Times New Roman", serif; font-size: 25px; line-height: 32px; color: var(--ink); }
  .photo { position: absolute; left: 37px; width: 126px; border-radius: 12px; }
  .photo-staff { top: 352px; height: 134px; background: linear-gradient(160deg, #d9c7b3, #2a2d36 70%); }
  .photo-interior { top: 502px; height: 132px; background: linear-gradient(160deg, #cfc8bc, #5b6a55 60%, #2b2e2f); }
  .photo-storefront { top: 652px; height: 134px; background: linear-gradient(180deg, #dfe3e6, #3a3f44 55%, #1d1f21); }
  .photo-platter { top: 803px; height: 134px; background: linear-gradient(150deg, #3e4a2a, #c27c4f 55%, #5a3a24); }

  .menu { position: absolute; left: 175px; top: 0; width: 698px; height: 1113px; }
  .price-band { position: absolute; left: 578px; top: 38px; width: 82px; height: 1075px; background: var(--price-band); }
  .title-bar { position: absolute; left: 0; top: 0; width: 698px; height: 38px; background: var(--black); color: var(--paper); font-weight: 700; font-size: 20.5px; line-height: 38px; padding-left: 28px; }

  .sections { position: absolute; left: 0; top: 38px; width: 698px; }
  .section { position: relative; border-bottom: 1px solid var(--rule); padding-top: 10px; }
  .section:last-child { border-bottom: none; }
  .line { position: relative; height: 17.5px; font-size: 13px; line-height: 17.5px; padding-left: 28px; }
  .line.sub { padding-left: 81px; }
  .line.intro { color: var(--muted); font-size: 14.5px; height: 22px; line-height: 22px; }
  .price { position: absolute; left: 578px; width: 82px; top: 0; text-align: center; font-weight: 700; }

  .footer-bar { position: absolute; left: 0; top: 1113px; width: 873px; height: 87px; background: var(--black); color: var(--paper); font-weight: 700; font-size: 31px; line-height: 60px; text-align: center; padding-top: 2px; }
</style>
</head>
<body>
  <aside class="sidebar">
    <div class="brand">
      <span class="brand-dot"></span>
      <div class="brand-name">Harlow Bean<br>Roasters</div>
    </div>
    <p class="order-note">Please<br>order<br>at counter</p>
    <div class="photo photo-staff" role="img" aria-label="Barista in a branded black t-shirt, seen from behind"></div>
    <div class="photo photo-interior" role="img" aria-label="Collage of the cafe interior, plants and coffee on tables"></div>
    <div class="photo photo-storefront" role="img" aria-label="Cafe storefront and counter seen from the street"></div>
    <div class="photo photo-platter" role="img" aria-label="Breakfast platter with smoked salmon, greens and toast on a wooden board"></div>
  </aside>

  <main class="menu">
    <div class="price-band"></div>
    <h1 class="title-bar">All day breakfast and Sandwich and Toast</h1>
    <div class="sections">
      <section class="section" style="height:96px;padding-top:9px">
        <p class="line intro">We use sourdough, panini and brioche buns from The Flour &amp; Hearth Bakery</p>
        <p class="line">Sourdough toast with butter/ jam/peanut butter/yeast spread<span class="price">1 for $3</span></p>
        <p class="line sub">-&nbsp; Cranberry, raisin &amp; fig<span class="price">2 for $5</span></p>
        <p class="line sub">-&nbsp; Wholemeal</p>
      </section>
      <section class="section" style="height:106px;padding-top:11px">
        <p class="line">Toasted fruit loaf with butter<span class="price">$5</span></p>
        <p class="line sub">-&nbsp; Banana bread</p>
        <p class="line sub">-&nbsp; Fruit &amp; nut bread</p>
        <p class="line sub">-&nbsp; Blueberry banana bread</p>
        <p class="line sub">-&nbsp; Pear &amp; raspberry bread</p>
      </section>
      <section class="section" style="height:107px">
        <p class="line">Pancake with maple syrup, vanilla ice cream &amp; fresh cut banana<span class="price">$15</span></p>
        <p class="line">Poppy seed / blueberry bagel with cream cheese<span class="price">$5</span></p>
        <p class="line">Poppy seed bagel with smoked Tasmania salmon &amp; cream cheese<span class="price">$9</span></p>
        <p class="line">Low fat Greek yogurt<span class="price">$8</span></p>
        <p class="line">with banana, toasted muesli, honey &amp; cinnamon</p>
      </section>
      <section class="section" style="height:192px">
        <p class="line">Smoked ham &amp; tasty cheese croissant<span class="price">$6.5</span></p>
        <p class="line">Tasty cheese &amp; tomato croissant<span class="price">$6.5</span></p>
        <p class="line">Date Scone with jam &amp; fresh cream<span class="price">$4.5</span></p>
        <p class="line">Wholemeal sourdough sandwiches:<span class="price">$8.5</span></p>
        <p class="line sub">- Turkey, rocket &amp; cranberry</p>
        <p class="line sub">- leg ham, cheese, avocado &amp; rocket</p>
        <p class="line sub">- Smoked salmon, feta, avocado &amp; rocket</p>
        <p class="line sub">- Sicilian tuna, boiled eggs &amp; rockets</p>
        <p class="line sub">- Char-grilled eggplant &amp; zucchini, Feta, pesto&amp; rocket</p>
        <p class="line sub">- Smoked chicken breast, cheese, avocado &amp; rocket</p>
      </section>
      <section class="section" style="height:54px">
        <p class="line">Hash brown, grilled haloumi, greenolive, sourdough &amp; lemon wedge<span class="price">$15</span></p>
        <p class="line">With Tasmania smoked salmon OR breakfast sausage</p>
      </section>
      <section class="section" style="height:122px">
        <p class="line">Breakfast with EGGS</p>
        <p class="line">2 poached or scrambled eggs with wholemeal sourdough<span class="price">$10</span></p>
        <p class="line">Extras:</p>
        <p class="line sub">-&nbsp; Avocado<span class="price">$3</span></p>
        <p class="line sub">-&nbsp; Bacon rasher<span class="price">$4</span></p>
        <p class="line sub">-&nbsp; Smoked salmon<span class="price">$5</span></p>
      </section>
      <section class="section" style="height:54px">
        <p class="line">Bacon &amp; eggs panini<span class="price">$8.5</span></p>
        <p class="line">Bacon rasher, fried eggs, tasty cheese &amp; avocado</p>
      </section>
      <section class="section" style="height:53px">
        <p class="line">Double bacon, egg&amp; hash brown roll<span class="price">$10</span></p>
        <p class="line">Grilled bacon rashers, fried eggs, tasty cheese &amp; hash brown on brioche</p>
      </section>
      <section class="section" style="height:52px">
        <p class="line">Tropical omelette with toasted sourdough<span class="price">$13</span></p>
        <p class="line">Pineapple, mushroom, leg ham, basil&amp; shredded cheese</p>
      </section>
      <section class="section" style="height:70px">
        <p class="line">Eggs benedict<span class="price">$13</span></p>
        <p class="line">Two poached eggs, Smoked Tasmanian salmon OR</p>
        <p class="line">smoked leg ham, Rocket &amp; house hollandaise on sourdough</p>
      </section>
      <section class="section" style="height:72px">
        <p class="line">Harlow well-being brekky<span class="price">$18</span></p>
        <p class="line">Tasmanian smoked salmon, boiled eggs salad with pesto, grilled tomato,</p>
        <p class="line">char-grilled pickled zucchini, string beans, rocket salad &amp; sourdough</p>
      </section>
      <section class="section" style="height:97px;padding-top:8px">
        <p class="line">Harlow mighty brekky<span class="price">$18</span></p>
        <p class="line">Free range scrambled eggs, bacon rasher, breakfast sausage, portaitomushroom,</p>
        <p class="line">grilled tomato &amp;sourdough</p>
      </section>
    </div>
  </main>

  <footer class="footer-bar">All day breakfast and Sandwich and Toast</footer>
</body>
</html>
```